shopfitters cards and stationery
Stationery
Project: shopfitters cards and stationery
shopfitters cards and stationery  - Construction
Creative Brief
Professional
Mark Pelling
Contracts Manager
7/24 Quarry Lane Wendale 4182
mark@fitwrightgroup.com.au
www.fitwrightgroup.com.au
Phone numbers and other details etc will change if you could use them for know that will be great. give me your best work :) Thanks

```html
<!DOCTYPE html>
<html lang="en">
<head>
<meta charset="utf-8">
<title>Fitwright Group – Business Card</title>
<link href="https://fonts.googleapis.com/css2?family=Exo+2:wght@400;600&display=swap" rel="stylesheet">
<style>
  :root{
    --bg:#d9d9da;
    --card-white:#ffffff;
    --blue-deep:#0b1f8f;
    --blue-mid:#1c3ec4;
    --blue-light:#3a63e0;
    --brand-blue:#1d3aa8;
    --frame-grey:#b9bcc4;
    --text-white:#ffffff;
  }
  *{margin:0;padding:0;box-sizing:border-box}
  html,body{width:1200px;height:908px;overflow:hidden;background:var(--bg);font-family:"Exo 2",sans-serif}
  .stage{position:relative;width:1200px;height:908px}
  .card{position:absolute;left:330px;width:540px;height:310px;border-radius:4px;box-shadow:0 6px 18px rgba(0,0,0,.18);overflow:hidden}
  .card--front{top:80px;background:var(--card-white);display:flex;align-items:center;justify-content:center}
  .card--back{top:480px;background:var(--frame-grey);padding:10px}

  .brand-name{color:var(--brand-blue);font-weight:600;white-space:nowrap;letter-spacing:1px}
  .card--front .brand-name{font-size:40px}

  .back-inner{position:relative;width:100%;height:100%;display:flex}
  .back-panel{flex:1;background:radial-gradient(ellipse at 45% 40%,var(--blue-light) 0%,var(--blue-mid) 40%,var(--blue-deep) 100%);position:relative;color:var(--text-white)}
  .back-side{width:150px;background:var(--card-white);display:flex;align-items:flex-end;justify-content:center;padding-bottom:30px;position:relative}
  .back-side::before{content:"";position:absolute;left:-12px;top:40px;border-style:solid;border-width:12px 12px 12px 0;border-color:transparent var(--card-white) transparent transparent}
  .back-side .brand-name{font-size:15px;letter-spacing:.5px}

  .contacts{position:absolute;left:26px;top:26px;list-style:none;font-size:12px;font-variant:all-small-caps;letter-spacing:1.2px;line-height:20px}
  .contacts li{display:flex;align-items:center;gap:8px}
  .contacts svg{width:12px;height:12px;flex:none}
  .person{position:absolute;right:22px;bottom:40px;text-align:right;font-variant:small-caps;letter-spacing:1.4px}
  .person__name{font-size:17px;font-weight:600}
  .person__role{font-size:12px}
</style>
</head>
<body>
<main class="stage">
  <section class="card card--front">
    <div class="brand-name">Fitwright Group</div>
  </section>

  <section class="card card--back">
    <div class="back-inner">
      <div class="back-panel">
        <ul class="contacts">
          <li><svg viewBox="0 0 12 12"><circle cx="6" cy="6" r="6" fill="#fff"/><path d="M6 2.5a2 2 0 0 1 2 2c0 1.5-2 4-2 4s-2-2.5-2-4a2 2 0 0 1 2-2z" fill="#1c3ec4"/></svg>7/24 Quarry Lane</li>
          <li><svg viewBox="0 0 12 12"><circle cx="6" cy="6" r="6" fill="#fff"/></svg>Wendale 4182</li>
          <li><svg viewBox="0 0 12 12"><circle cx="6" cy="6" r="6" fill="#fff"/><path d="M4 3l1.3 1.6-.7.8a5 5 0 0 0 2 2l.8-.7L9 8l-1 1c-2.5 0-5-2.5-5-5z" fill="#1c3ec4"/></svg>T 07 3555 0142</li>
          <li><svg viewBox="0 0 12 12"><circle cx="6" cy="6" r="6" fill="#fff"/></svg>F 07 3555 0143</li>
          <li><svg viewBox="0 0 12 12"><circle cx="6" cy="6" r="6" fill="#fff"/></svg>M 0400 555 218</li>
          <li><svg viewBox="0 0 12 12"><circle cx="6" cy="6" r="6" fill="#fff"/><rect x="3" y="4" width="6" height="4" fill="#1c3ec4"/></svg>mark@fitwrightgroup.com.au</li>
          <li><svg viewBox="0 0 12 12"><circle cx="6" cy="6" r="6" fill="#fff"/><circle cx="6" cy="6" r="3" fill="none" stroke="#1c3ec4"/></svg>www.fitwrightgroup.com.au</li>
        </ul>
        <div class="person">
          <div class="person__name">Mark Pelling</div>
          <div class="person__role">Contracts Manager</div>
        </div>
      </div>
      <div class="back-side">
        <div class="brand-name">Fitwright Group</div>
      </div>
    </div>
  </section>
</main>
</body>
</html>
```